Cardiology practice business card

We need a business card for our cardiology practice "Bellmoor Cardiology". We have a new logo, attached below. We like the colours in the logo - red and charcoal. The front of the business card will need to have the doctors name, address, phone number and email. The back will need to have space to write 2 appointment dates and times.

```html
<!DOCTYPE html>
<html lang="en">
<head>
<meta charset="utf-8">
<title>Bellmoor Cardiology – Business Card</title>
<link rel="stylesheet" href="https://fonts.googleapis.com/css2?family=Montserrat:wght@400;500;600;700&display=swap">
<style>
  :root {
    --backdrop: #e5e5e5;
    --paper: #ffffff;
    --charcoal: #36393c;
    --ink: #3a3a3a;
    --ink-soft: #5f6062;
    --red: #d71920;
  }
  * { box-sizing: border-box; margin: 0; padding: 0; }
  html, body {
    width: 1046px; height: 1200px; overflow: hidden;
    background: var(--backdrop);
    font-family: "Montserrat", sans-serif;
  }
  .card {
    position: absolute; left: 223px;
    width: 601px; height: 381px;
    background: var(--paper);
    overflow: hidden;
  }
  .card--front { top: 139px; }
  .card--back { top: 628px; }

  .wordmark {
    position: absolute;
    color: var(--red);
    font-weight: 700;
    text-transform: uppercase;
    line-height: 1.05;
  }
  .card--front .wordmark {
    right: 43px; top: 60px;
    font-size: 30px; letter-spacing: 2px; text-align: right;
  }
  .card--back .wordmark {
    left: 36px; top: 50px;
    font-size: 28px; letter-spacing: 2px;
  }

  .doctor { position: absolute; left: 42px; top: 140px; color: var(--ink); }
  .doctor__name { color: var(--red); font-weight: 700; font-size: 22px; line-height: 1.1; }
  .doctor__credentials { font-weight: 700; font-size: 16px; margin-top: 3px; }
  .doctor__role { font-size: 17px; line-height: 1.25; margin-top: 3px; }

  .contact {
    position: absolute; right: 42px; top: 221px;
    text-align: right; color: var(--ink); font-size: 17px; line-height: 1.25;
  }
  .contact__phone { font-weight: 700; font-size: 19px; color: var(--ink-soft); }
  .contact__email { margin-top: 8px; }
  .contact__address { margin-top: 13px; }
  .contact__web { margin-top: 9px; color: var(--red); font-weight: 700; }

  .back-band { position: absolute; left: 0; top: 0; width: 601px; height: 186px; }
  .back-address {
    position: absolute; right: 31px; top: 68px;
    color: #fff; font-size: 17px; line-height: 1.25; text-align: right;
  }
  .appointment-title {
    position: absolute; right: 33px; top: 160px;
    color: var(--red); font-weight: 700; font-size: 24px; letter-spacing: 3.5px;
  }
  .appointment-row {
    position: absolute; left: 38px; width: 524px;
    display: flex; align-items: baseline;
    font-size: 17px; color: #111;
  }
  .appointment-row--first { top: 247px; }
  .appointment-row--second { top: 305px; }
  .appointment-row .label { margin-right: 6px; }
  .appointment-row .blank { border-bottom: 1.5px dotted #111; height: 1px; }
  .appointment-row .blank--date { width: 238px; margin-right: 7px; }
  .appointment-row .blank--time { flex: 1; }
</style>
</head>
<body>

<section class="card card--front">
  <div class="wordmark">Bellmoor<br>Cardiology</div>

  <div class="doctor">
    <div class="doctor__name">Dr Elliot Marsh</div>
    <div class="doctor__credentials">MBBS, FRACP</div>
    <div class="doctor__role">Consultant Cardiologist<br>&amp; Physician</div>
  </div>

  <div class="contact">
    <div class="contact__phone">(07) 4100 2846</div>
    <div class="contact__email">reception@bellmoorcardio.com.au</div>
    <div class="contact__address">Level 2, Bellmoor Private Hospital<br>27 Harbour Road, Bellmoor QLD</div>
    <div class="contact__web">www.bellmoorcardiology.com.au</div>
  </div>
</section>

<section class="card card--back">
  <svg class="back-band" viewBox="0 0 601 186" aria-hidden="true">
    <path d="M0 0 H601 V134 H423 C370 134 335 150 292 186 H0 Z" fill="var(--charcoal)"/>
  </svg>

  <div class="wordmark">Bellmoor<br>Cardiology</div>

  <div class="back-address">Level 2, Bellmoor Private Hospital<br>27 Harbour Road, Bellmoor QLD</div>

  <div class="appointment-title">APPOINTMENT</div>

  <div class="appointment-row appointment-row--first">
    <span class="label">DATE</span><span class="blank blank--date"></span>
    <span class="label">TIME</span><span class="blank blank--time"></span>
  </div>
  <div class="appointment-row appointment-row--second">
    <span class="label">DATE</span><span class="blank blank--date"></span>
    <span class="label">TIME</span><span class="blank blank--time"></span>
  </div>
</section>

</body>
</html>
```